Business Card Design Project

I want a cleaner business card and envelope then what we have now, its too crowded.
Updates

I update with logo, this can be changed anyway you feel it looks best. I also have put gaurantee on there and extended time, this is my first time doing this. Also gave an example of current card

Target Market(s)

a wide array of customers from lattice 700 to small companies and cleints

Industry/Entity Type

Business

Requirements
Must have
• Need to have address, telephone number email
Nice to have
• a sharp professional card that stands out but is still very clean.
Should not have
• Not crazy looking

```html
<!DOCTYPE html>
<html lang="en">
<head>
<meta charset="utf-8">
<title>Meridian Assurance Group — Stationery</title>
<link rel="stylesheet" href="https://fonts.googleapis.com/css2?family=Arimo:wght@400;700&family=Tinos:wght@400;700&display=swap">
<style>
  :root {
    --bg: #ffffff;
    --paper: #ffffff;
    --ink: #111111;
    --ink-soft: #333333;
    --mark: #6e6e6e;
    --band: #111111;
    --silver-dark: #5a5a5a;
    --silver-light: #e6e6e6;
    --edge: #d9d9d9;
  }
  * { box-sizing: border-box; margin: 0; padding: 0; }
  html, body { width: 1200px; height: 900px; overflow: hidden; background: var(--bg); }
  .canvas { position: relative; width: 1200px; height: 900px; }

  /* Letterhead */
  .letterhead {
    position: absolute; left: 560px; top: 110px; width: 500px; height: 680px;
    background: var(--paper); border: 1px solid var(--edge);
    font-family: "Arimo", Arial, sans-serif; color: var(--ink);
  }
  .brand { display: flex; align-items: center; gap: 8px; }
  .brand-square { width: 22px; height: 22px; background: var(--mark); flex: none; }
  .brand-name { font-family: "Arimo", Arial, sans-serif; font-size: 11px; letter-spacing: 1.5px; text-transform: uppercase; color: var(--ink-soft); line-height: 1.25; }
  .letterhead .brand { position: absolute; left: 36px; top: 44px; }
  .letterhead .brand-name { width: 110px; }
  .letterhead-contact {
    position: absolute; right: 24px; top: 50px; text-align: right;
    font-size: 9.5px; line-height: 12px; font-style: normal;
  }
  .letter-body { position: absolute; left: 22px; top: 160px; width: 460px; font-size: 12px; line-height: 17px; }
  .letter-body p + p { margin-top: 16px; }
  .letter-body .gap { margin-top: 36px; }
  .letterhead-band { position: absolute; left: 0; bottom: 28px; width: 300px; height: 10px; background: var(--band); }
  .letterhead-sheen { position: absolute; right: 0; bottom: 28px; width: 95px; height: 10px;
    background: linear-gradient(90deg, var(--silver-dark), var(--silver-light) 50%, var(--silver-dark)); }

  /* Business cards */
  .card {
    position: absolute; width: 380px; height: 217px; background: var(--paper);
    border: 1px solid var(--edge); overflow: hidden;
  }
  .card-front { left: 110px; top: 170px; }
  .card-back { left: 110px; top: 450px; }

  .card-front .brand { position: absolute; left: 150px; top: 30px; }
  .card-front .brand-name { font-family: "Tinos", "Times New Roman", serif; font-size: 14px; width: 160px; letter-spacing: 2px; }
  .card-accent { position: absolute; left: 0; top: 130px; width: 8px; height: 87px; background: var(--band); }
  .card-contact {
    position: absolute; left: 40px; top: 122px; width: 120px; text-align: right;
    font-family: "Tinos", "Times New Roman", serif; font-size: 8.5px; line-height: 10.5px; font-style: normal; color: var(--ink-soft);
  }
  .nameplate {
    position: absolute; left: 172px; top: 110px; width: 208px; height: 60px;
    background: linear-gradient(180deg, var(--silver-light), var(--silver-dark) 55%, var(--silver-light));
    padding: 10px 0 0 18px; color: #ffffff; font-family: "Tinos", "Times New Roman", serif;
  }
  .nameplate-name { font-size: 22px; line-height: 24px; }
  .nameplate-title { font-size: 8px; letter-spacing: 2px; text-transform: uppercase; }

  .card-back .brand { position: absolute; left: 0; right: 0; top: 70px; justify-content: center; }
  .card-back .brand-square { width: 30px; height: 30px; }
  .card-back .brand-name { font-size: 15px; letter-spacing: 2.5px; }
  .card-stripe { position: absolute; left: 0; bottom: 36px; width: 100%; height: 6px; background: var(--silver-dark); }
  .card-band {
    position: absolute; left: 0; bottom: 0; width: 100%; height: 36px; background: var(--band);
    color: #ffffff; font-family: "Arimo", Arial, sans-serif; font-size: 10px;
    display: flex; align-items: center; justify-content: flex-end; padding-right: 26px;
  }
</style>
</head>
<body>
<main class="canvas">

  <section class="card card-front" aria-label="Business card, front">
    <div class="brand">
      <span class="brand-square"></span>
      <span class="brand-name">Meridian Assurance Group</span>
    </div>
    <span class="card-accent"></span>
    <address class="card-contact">
      PO Box 204810<br>
      Austin, TX 78701<br>
      (555) 014-2290<br>
      dkessler@meridianag.com<br>
      www.meridianag.com
    </address>
    <div class="nameplate">
      <div class="nameplate-name">Dana Kessler</div>
      <div class="nameplate-title">President</div>
    </div>
  </section>

  <section class="card card-back" aria-label="Business card, back">
    <div class="brand">
      <span class="brand-square"></span>
      <span class="brand-name">Meridian Assurance Group</span>
    </div>
    <span class="card-stripe"></span>
    <div class="card-band">www.meridianassurancegroup.com</div>
  </section>

  <section class="letterhead" aria-label="Letterhead">
    <div class="brand">
      <span class="brand-square"></span>
      <span class="brand-name">Meridian Assurance Group</span>
    </div>
    <address class="letterhead-contact">
      PO Box 204810<br>
      Austin, TX 78701<br>
      (555) 014-2290<br>
      office@meridianag.com<br>
      www.meridianag.com
    </address>
    <div class="letter-body">
      <p>Lorem ipsum dolor sit amet, consectetur adipiscing elit. Mauris a nibh. Nulla mattis molestie tellus. Vestibulum massa diam, tempus a, content link feugiata, elit. Nunc commodo justo a tellus. Cras volutpat. Integer tellus est, molestie ut, pellentesque at, euismod sodales, lacus. Pellentesque</p>
      <p>mollis enim. Nulla vel enim non ligula viverra fringilla. Nam iaculis. Pellentesque ut ante sed mi mattis pharetra. Cras viverra turpis bibendum nisl. Proin vitae turpis. Integer diam sem, aliquet sit amet, condimentum vitae, varius vel, gravida, orci id consectetur laoreet, ligula sem pretium odio, condimentum blandit</p>
      <p class="gap">Lorem ipsum dolor sit amet, consectetur adipiscing elit. Mauris a nibh. Nulla mattis molestie tellus. Vestibulum massa diam, tempus a, content link feugiata, elit. Nunc commodo justo a tellus. Cras volutpat. Integer tellus est, molestie ut, pellentesque at, euismod sodales, lacus. Pellentesque</p>
      <p>mollis enim. Nulla vel enim non ligula viverra fringilla. Nam iaculis. Pellentesque ut ante sed mi mattis pharetra. Cras viverra turpis bibendum nisl. Proin vitae turpis. Integer diam sem, aliquet sit amet, condimentum vitae, varius vel, gravida, orci id consectetur laoreet, ligula sem pretium odio, condimentum blandit risus urna quis diam.</p>
    </div>
    <span class="letterhead-band"></span>
    <span class="letterhead-sheen"></span>
  </section>

</main>
</body>
</html>
```